Book Cover Design - Uncovering Weight Loss Secrets

I need a book cover design for a book called 'Folding The Map'. It is a book that goes through all of the secrets to weight loss, without any crazy shakes or workouts or pills or potions. The book is really focused on helping people understand that Weight loss is simple and has more to do with our mindset as well as the food we were eating. It is about taking personal responsibility not looking for the next fancy revolutionary product that is going to help them magically melt the fat away. The book is pragmatic in nature and breaks down in simple terms how we can lose weight and keep it off for the rest of our lives. It shows the user that it is simple to lose weight, but it takes effort. They should stop looking for a quick fix when it comes to weight loss but instead eat healthy for the rest of their lives.
The book is intended to be hard-hitting no holds barred approach. The book has the same title as my business name. I will attach the current logo that we use in the business. This doesn't need to be on the front of the book maybe at the back down the bottom somewhere.
I am looking to have both an e-book cover and a standard printed book cover.
I don't have any colours in mind, my logo can be adapted to be different colours or just white.
The message that I am wanting people to feel when they see my book, is that all these Weightloss fads are a joke, that I know the secrets that will get them to their weight loss goal even if they fail at everything else before.
On the cover it should say the following.
FOLDING THE MAP
Uncovering the Weight Loss Secrets
The big companies have been trying to keep hidden for years!
COLIN MAYHEW
People who have failed many times trying to lose weight & need help
Weight Loss

```html
<!DOCTYPE html>
<html lang="en">
<head>
<meta charset="UTF-8">
<title>Folding The Map – Book Cover</title>
<link href="https://fonts.googleapis.com/css2?family=Poppins:wght@400;500;700&display=swap" rel="stylesheet">
<style>
  :root {
    --leaf-deep: #0b1a0f;
    --leaf-mid: #1f4a28;
    --leaf-light: #3a6b3a;
    --curtain-red: #c4231c;
    --curtain-orange: #e9861e;
    --curtain-dark: #6e130f;
    --title-white: #ffffff;
    --accent-orange: #e58a26;
    --tagline-white: #eef0ea;
  }
  html, body {
    margin: 0;
    padding: 0;
    width: 800px;
    height: 1200px;
    overflow: hidden;
    background: var(--leaf-deep);
  }
  .cover {
    position: relative;
    width: 800px;
    height: 1200px;
    overflow: hidden;
    font-family: 'Poppins', sans-serif;
  }
  .cover-art {
    position: absolute;
    inset: 0;
    width: 800px;
    height: 1200px;
  }
  .title-block {
    position: absolute;
    left: 68px;
    top: 640px;
    width: 420px;
  }
  .book-title {
    margin: 0;
    color: var(--title-white);
    font-weight: 700;
    font-size: 36px;
    letter-spacing: 2.6px;
    line-height: 1;
  }
  .book-subtitle {
    margin: 8px 0 0;
    color: var(--accent-orange);
    font-weight: 500;
    font-size: 19px;
    letter-spacing: 0.6px;
    line-height: 1.2;
  }
  .book-teaser {
    margin: 10px 0 0;
    color: var(--tagline-white);
    font-weight: 400;
    font-size: 13px;
    letter-spacing: 0.6px;
    line-height: 19px;
  }
  .tagline {
    position: absolute;
    left: 0;
    right: 0;
    top: 1088px;
    margin: 0;
    text-align: center;
    color: var(--tagline-white);
    font-weight: 400;
    font-size: 15.5px;
    letter-spacing: 0.9px;
    line-height: 27px;
  }
  .author {
    position: absolute;
    left: 0;
    right: 0;
    top: 1154px;
    margin: 0;
    text-align: center;
    color: var(--title-white);
    font-weight: 700;
    font-size: 14px;
    letter-spacing: 2px;
  }
</style>
</head>
<body>
  <main class="cover">
    <svg class="cover-art" viewBox="0 0 800 1200" xmlns="http://www.w3.org/2000/svg">
      <defs>
        <radialGradient id="foliage-tone" cx="0.25" cy="0.4" r="0.85">
          <stop offset="0" stop-color="#3a6b3a"/>
          <stop offset="0.45" stop-color="#1f4a28"/>
          <stop offset="1" stop-color="#0b1a0f"/>
        </radialGradient>
        <linearGradient id="curtain-tone" x1="0" y1="0" x2="1" y2="1">
          <stop offset="0" stop-color="#e9861e"/>
          <stop offset="0.35" stop-color="#c4231c"/>
          <stop offset="0.7" stop-color="#e9861e"/>
          <stop offset="1" stop-color="#6e130f"/>
        </linearGradient>
      </defs>
      <rect class="foliage-backdrop" x="0" y="0" width="800" height="1200" fill="url(#foliage-tone)" role="img" aria-label="Dense dark green monstera leaves filling the background"/>
      <path class="fruit-curtain" d="M336 0 C 360 200, 430 420, 492 600 C 540 760, 590 900, 610 980 C 640 1080, 690 1160, 708 1200 L 800 1200 L 800 0 Z" fill="url(#curtain-tone)" role="img" aria-label="Sheer curtain printed with strawberries and orange slices, drawn back from the right"/>
    </svg>

    <header class="title-block">
      <h1 class="book-title">FOLDING THE MAP</h1>
      <p class="book-subtitle">Uncovering the Weight Loss Secrets</p>
      <p class="book-teaser">The big companies have been trying<br>to keep hidden for years!</p>
    </header>

    <p class="tagline">For Losing All The Weight You Want &amp; Keeping It Off Forever<br>No Matter What You Have Tried in The Past</p>
    <p class="author">COLIN MAYHEW</p>
  </main>
</body>
</html>
```